App Design for FlavorTrek

We need an app design for a new app called FlavorTrek, which is an app designed to inspire exploration through personalized recipe generation, local restaurant discoveries, and a vibrant community platform. It caters to food enthusiasts looking to explore global cuisines or find the best local dining spots, offering a premium experience with selected features available for free.

-------UPDATED-----
This app will be AI Driven and may not be heavily dependent on media (images,videos) at first, especially for the Recipe generator feature. Our goal is to still have attractive UI. The core functionalities we are looking are the following
1. Recipe Generator: Either user choose a specific cuisine(italian,spanish), or user inputs ingredients and get recipe, or get recipe for different occasions (xmas, thanksgiving ) and get a randomly get recipe to cook, plain simple. We expect the recipes to be displayed in clear and not too generic manner starting with ingredients and expected duration at top and then step by step guide. We also intend to enable premium users to have playful action button or icon to get unlimited recipes generated until they find what they like and also have save for later feature. These premium features should be disabled for free users and prompted to subscribe if they click them with nice popup
2. Restaurant Recommendation - will have selected pictures and will be based on inputs such as zip code and other filters such as cousine types. Premium users can filter by price range, get unlimited recommendation, see actual price range in the recommendation and can save for later where they can find it later. Free users cannot filter by price (disabled) and should see it hidden in the recommendation
3. Meal Planning - will include just simple and random meal plan with just one button or limited interaction for free, users need to subscribe to get features such as customized plan such as considering allergies or diet preferences. Premium users can also get a shopping checklist of ingredients for weekly meal preps and their step by step guide for each meal recipe.
2. Community Sharing: users can view posts and engage with community content
Updates

Hello Designers,

The initial price was not fair for the work. So I have increased it. There will also be $50-100 bonus for those who come up with great designs or for those who incorporate interesting stuff. Thank you! Much appreciated 🙏

Colors
0054AA
0677BA
7BADD7
CADEEF
E8F1F8
0094D4
00A9DD
6FCCEA
C7EBF8
E9F6FB
00AB8E
00BBA5
67D7C9
C6EFE9
E9F9F6
FFC000
F8CF3A
FAE287
FDF2CF
FEFAEE
F0912C
F2A743
F7CA91
FBE8D2
FDF5EE
EE7325
F08F49
F5BC92
FAE3D3
FDF4ED
A7469A
B969AE
D3A5CF
EDDBEB
F8F0F9
6B429C
8869AF
B7A5CE
E3DAEB
F3F0F8

```html
<!DOCTYPE html>
<html lang="en">
<head>
<meta charset="utf-8">
<title>FlavorTrek — Recipes and Restaurants</title>
<link rel="stylesheet" href="https://fonts.googleapis.com/css2?family=Plus+Jakarta+Sans:wght@400;500;600;700;800&display=swap">
<style>
  :root {
    --page: #ffffff;
    --screen: #fffcf9;
    --ink: #2f3337;
    --muted: #5b5f63;
    --placeholder: #55595d;
    --orange: #ff774c;
    --orange-soft: #fff0ea;
    --field: #fef3e1;
    --group-line: #f1eac6;
    --card: #fdf6ee;
    --divider: #f0ebe6;
    --tab-idle: #9a9da1;
    --photo-warm: #b7733f;
    --photo-dark: #5a3420;
    --photo-pizza: #c45a2f;
  }
  * { box-sizing: border-box; margin: 0; padding: 0; }
  html, body { width: 922px; height: 1200px; overflow: hidden; background: var(--page); }
  body { position: relative; font-family: "Plus Jakarta Sans", sans-serif; color: var(--ink); }

  .screen { position: absolute; top: 0; width: 430px; background: var(--screen); border-radius: 40px; overflow: hidden; box-shadow: 0 0 0 1px #eee8e2; }
  .screen--recipes { left: 10px; height: 1188px; }
  .screen--restaurant { left: 480px; height: 1030px; }
  .screen > * { position: absolute; }

  .status-time { top: 24px; left: 26px; font-size: 15px; font-weight: 700; }
  .status-icons { top: 25px; right: 38px; display: flex; gap: 8px; }

  .avatar { top: 70px; left: 16px; width: 48px; height: 48px; border-radius: 50%; background: radial-gradient(circle at 50% 40%, #c9a37e, #4f6b7c); }
  .crown { top: 84px; left: 331px; }
  .menu-button { top: 70px; left: 366px; width: 48px; height: 48px; border-radius: 50%; background: var(--orange); display: flex; align-items: center; justify-content: center; }

  .section-title { left: 16px; font-size: 16px; font-weight: 600; line-height: 20px; }

  .button { left: 16px; width: 398px; height: 56px; border-radius: 28px; display: flex; align-items: center; justify-content: center; gap: 8px; font-size: 16px; font-weight: 700; }
  .button--primary { background: var(--orange); color: #fff; }
  .button--outline { background: var(--orange-soft); color: var(--orange); border: 1.5px solid var(--orange); }

  .field-group { left: 16px; width: 398px; border: 1px solid var(--group-line); border-radius: 24px; }
  .field { position: absolute; left: 8px; right: 8px; top: 7px; height: 52px; border-radius: 26px; background: var(--field); font-size: 14px; color: var(--placeholder); display: flex; align-items: center; padding-left: 16px; }
  .field--plain { left: 16px; width: 398px; right: auto; }
  .chips { position: absolute; left: 8px; display: flex; gap: 9px; }
  .chip { height: 52px; border-radius: 26px; background: var(--field); font-size: 14px; font-weight: 600; color: var(--ink); display: flex; align-items: center; padding: 0 16px; gap: 8px; }
  .chip--selected { border: 1px solid var(--orange); font-weight: 700; }
  .chip--quiet { font-weight: 400; color: var(--placeholder); }
  .chip-remove { color: var(--orange); font-weight: 700; }

  .recipe-card { top: 882px; left: 16px; width: 398px; height: 118px; border-radius: 24px; background: var(--card); }
  .recipe-photo { position: absolute; left: 0; top: 0; width: 132px; height: 118px; border-radius: 24px; background: linear-gradient(135deg, var(--photo-pizza), var(--photo-warm) 55%, var(--photo-dark)); }
  .recipe-name { position: absolute; left: 134px; top: 12px; font-size: 19px; font-weight: 700; }
  .recipe-ingredients { position: absolute; left: 134px; top: 43px; font-size: 12px; color: var(--muted); }
  .meta { position: absolute; display: flex; align-items: center; gap: 5px; font-size: 12px; color: var(--ink); }

  .bookmark-button { top: 1012px; left: 362px; width: 52px; height: 52px; border-radius: 50%; border: 1.5px solid var(--orange); display: flex; align-items: center; justify-content: center; }

  .restaurant-card { top: 670px; width: 296px; height: 236px; border-radius: 24px; background: var(--card); overflow: hidden; }
  .restaurant-photo { position: absolute; top: 0; left: 0; width: 100%; height: 118px; background: linear-gradient(160deg, #e5c7a2, var(--photo-warm) 50%, #6b3f26); }
  .save-badge { position: absolute; top: 10px; right: 10px; width: 40px; height: 40px; border-radius: 50%; background: #fff; display: flex; align-items: center; justify-content: center; }
  .restaurant-name { position: absolute; left: 16px; top: 130px; font-size: 19px; font-weight: 700; white-space: nowrap; }
  .restaurant-address { position: absolute; left: 16px; top: 161px; font-size: 12px; color: var(--muted); white-space: nowrap; }

  .tab-bar { left: 0; width: 430px; height: 72px; border-top: 1px solid var(--divider); }
  .tab { position: absolute; top: 14px; width: 90px; margin-left: -45px; display: flex; flex-direction: column; align-items: center; gap: 5px; font-size: 12px; color: var(--tab-idle); }
  .tab--active { color: var(--orange); font-weight: 600; }
</style>
</head>
<body>

<!-- Recipes screen -->
<section class="screen screen--recipes" aria-label="Recipe generator">
  <span class="status-time">9:41</span>
  <span class="status-icons">
    <svg width="20" height="14" viewBox="0 0 20 14" fill="none" stroke="#2f3337" stroke-width="1.8"><path d="M1 5a13 13 0 0 1 18 0M4 8a8.5 8.5 0 0 1 12 0M7 11a4 4 0 0 1 6 0"/></svg>
    <svg width="22" height="14" viewBox="0 0 22 14" fill="none" stroke="#2f3337" stroke-width="1.5"><rect x="1" y="1.5" width="17" height="11" rx="3"/><rect x="4" y="4.5" width="5" height="5" fill="#2f3337" stroke="none"/><path d="M20 5.5v3"/></svg>
  </span>

  <div class="avatar" role="img" aria-label="User profile photo"></div>
  <svg class="crown" width="20" height="20" viewBox="0 0 20 20" fill="none" stroke="#ff774c" stroke-width="1.5" stroke-linejoin="round"><path d="M3 7l4 3 3-6 3 6 4-3-1.5 9h-11z"/><circle cx="10" cy="12.5" r="0.8" fill="#ff774c"/></svg>
  <div class="menu-button"><svg width="18" height="16" viewBox="0 0 18 16" stroke="#fff" stroke-width="1.8" stroke-linecap="round"><path d="M1 2h16M1 8h11M1 14h16"/></svg></div>

  <h2 class="section-title" style="top:154px">Random recipe</h2>
  <div class="button button--outline" style="top:182px">
    <svg width="22" height="22" viewBox="0 0 22 22" fill="none" stroke="#ff774c" stroke-width="1.6" stroke-linecap="round"><path d="M3 19L13 9M13 9l1.5-1.5"/><path d="M15 2v4M13 4h4M19 8v3M17.5 9.5h3M8 3v2M7 4h2"/></svg>
    Surprise me
  </div>

  <h2 class="section-title" style="top:290px">Customise your recipe</h2>

  <div class="field-group" style="top:318px;height:128px">
    <div class="field">Add ingredients</div>
    <div class="chips" style="top:67px">
      <span class="chip"><span class="chip-remove">-</span>Egg</span>
      <span class="chip"><span class="chip-remove">-</span>Flour</span>
    </div>
  </div>

  <div class="field-group" style="top:454px;height:128px">
    <div class="field">Choose&nbsp; Couisine</div>
    <div class="chips" style="top:67px">
      <span class="chip chip--selected">Italian</span>
      <span class="chip chip--quiet" style="margin-left:2px">Spanish</span>
      <span class="chip chip--quiet">Indian</span>
    </div>
  </div>

  <div class="field-group" style="top:590px;height:68px">
    <div class="field">Choose different occasions</div>
  </div>

  <div class="field-group" style="top:666px;height:68px">
    <div class="field">Avoid ingridients</div>
  </div>

  <div class="button button--primary" style="top:746px">
    <svg width="22" height="22" viewBox="0 0 22 22" fill="none" stroke="#fff" stroke-width="1.6" stroke-linecap="round"><path d="M3 19L13 9M13 9l1.5-1.5"/><path d="M15 2v4M13 4h4M19 8v3M17.5 9.5h3M8 3v2M7 4h2"/></svg>
    Get your recipe
  </div>

  <h2 class="section-title" style="top:854px">Recipe result</h2>
  <article class="recipe-card">
    <div class="recipe-photo" role="img" aria-label="Photo of sliced pizza with peppers"></div>
    <h3 class="recipe-name">Pizza Recipes 01</h3>
    <p class="recipe-ingredients">2 Egg, 14g Flour, 150Ml Waters</p>
    <span class="meta" style="left:136px;top:86px">
      <svg width="14" height="14" viewBox="0 0 14 14" fill="none" stroke="#ff774c" stroke-width="1.3"><path d="M7 1c3 3 4.5 5 4.5 7.5A4.5 4.5 0 0 1 2.5 8.5C2.5 6.5 4 5 4.5 4c.5 1.5 1.5 2 2 2C6.5 4 7 2.5 7 1z"/></svg>330 Cal</span>
    <span class="meta" style="left:234px;top:86px">
      <svg width="14" height="14" viewBox="0 0 14 14" fill="none" stroke="#ff774c" stroke-width="1.3"><circle cx="7" cy="7" r="5.8"/><path d="M7 4v3.2l2 1.3"/></svg>15 Min</span>
    <span class="meta" style="left:322px;top:86px">
      <svg width="14" height="14" viewBox="0 0 14 14" fill="none" stroke="#ff774c" stroke-width="1.3"><circle cx="7" cy="7" r="5.8"/><circle cx="7" cy="5.8" r="1.8"/><path d="M3.6 11.2a4 4 0 0 1 6.8 0"/></svg>2 Pe</span>
  </article>

  <div class="button button--primary" style="top:1012px;width:338px;height:52px">Get new</div>
  <div class="bookmark-button"><svg width="14" height="18" viewBox="0 0 14 18"><path d="M2 1h10a1 1 0 0 1 1 1v15l-6-4-6 4V2a1 1 0 0 1 1-1z" fill="#ff774c"/></svg></div>

  <nav class="tab-bar" style="top:1116px">
    <span class="tab tab--active" style="left:62px">
      <svg width="22" height="22" viewBox="0 0 22 22" fill="none" stroke="#ff774c" stroke-width="1.5"><rect x="2" y="2" width="18" height="18" rx="5"/><path d="M7 9h8M7 13h5" stroke-linecap="round"/></svg>Recipes</span>
    <span class="tab" style="left:164px">
      <svg width="22" height="22" viewBox="0 0 22 22" fill="none" stroke="#9a9da1" stroke-width="1.5"><rect x="3" y="4" width="16" height="16" rx="3"/><path d="M8 2v4M14 2v4M7 15h8M11 8l3 4H8z"/></svg>Restaurant</span>
    <span class="tab" style="left:265px">
      <svg width="24" height="22" viewBox="0 0 24 22" fill="none" stroke="#9a9da1" stroke-width="1.5"><path d="M2 12h20a10 8 0 0 1-20 0zM4 12a8 7 0 0 1 16 0M12 3v2M8 8l2 2M16 8l-2 2"/></svg>Meal</span>
    <span class="tab" style="left:367px">
      <svg width="24" height="22" viewBox="0 0 24 22" fill="none" stroke="#9a9da1" stroke-width="1.5"><circle cx="9" cy="7" r="4"/><path d="M2 20a7 7 0 0 1 14 0zM15 3.5a4 4 0 0 1 0 7M18 14a6 6 0 0 1 4 6h-3"/></svg>Comm</span>
  </nav>
</section>

<!-- Restaurant screen -->
<section class="screen screen--restaurant" aria-label="Restaurant finder">
  <span class="status-time">9:41</span>
  <span class="status-icons">
    <svg width="20" height="14" viewBox="0 0 20 14" fill="none" stroke="#2f3337" stroke-width="1.8"><path d="M1 5a13 13 0 0 1 18 0M4 8a8.5 8.5 0 0 1 12 0M7 11a4 4 0 0 1 6 0"/></svg>
    <svg width="22" height="14" viewBox="0 0 22 14" fill="none" stroke="#2f3337" stroke-width="1.5"><rect x="1" y="1.5" width="17" height="11" rx="3"/><rect x="4" y="4.5" width="5" height="5" fill="#2f3337" stroke="none"/><path d="M20 5.5v3"/></svg>
  </span>

  <div class="avatar" role="img" aria-label="User profile photo"></div>
  <svg class="crown" width="20" height="20" viewBox="0 0 20 20" fill="none" stroke="#ff774c" stroke-width="1.5" stroke-linejoin="round"><path d="M3 7l4 3 3-6 3 6 4-3-1.5 9h-11z"/><circle cx="10" cy="12.5" r="0.8" fill="#ff774c"/></svg>
  <div class="menu-button"><svg width="18" height="16" viewBox="0 0 18 16" stroke="#fff" stroke-width="1.8" stroke-linecap="round"><path d="M1 2h16M1 8h11M1 14h16"/></svg></div>

  <h2 class="section-title" style="top:154px">Let’s get you a place to eat</h2>

  <div class="field field--plain" style="top:182px">Enter Zip code</div>

  <div class="field-group" style="top:242px;height:68px">
    <div class="field">Choose&nbsp; Couisine type</div>
  </div>

  <div class="field-group" style="top:318px;height:68px">
    <div class="field">Choose different occasions</div>
  </div>

  <div class="field field--plain" style="top:394px">Max Distance</div>

  <div class="field-group" style="top:454px;height:68px">
    <div class="chips" style="top:7px">
      <span class="chip chip--quiet">Min Price</span>
      <span class="chip chip--quiet">Max Price</span>
    </div>
  </div>

  <div class="button button--primary" style="top:534px">
    <svg width="22" height="22" viewBox="0 0 22 22" fill="none" stroke="#fff" stroke-width="1.6" stroke-linecap="round"><path d="M3 19L13 9M13 9l1.5-1.5"/><path d="M15 2v4M13 4h4M19 8v3M17.5 9.5h3M8 3v2M7 4h2"/></svg>
    Get your restaurant
  </div>

  <h2 class="section-title" style="top:642px">Nearby Restaurant</h2>

  <article class="restaurant-card" style="left:16px">
    <div class="restaurant-photo" role="img" aria-label="Photo of a warm restaurant dining room"></div>
    <div class="save-badge"><svg width="14" height="18" viewBox="0 0 14 18"><path d="M2 1h10a1 1 0 0 1 1 1v15l-6-4-6 4V2a1 1 0 0 1 1-1z" fill="#ff774c"/></svg></div>
    <h3 class="restaurant-name">Pizza Restaurant 01</h3>
    <p class="restaurant-address">Address 1234 N St</p>
    <span class="meta" style="left:16px;top:204px">
      <svg width="15" height="15" viewBox="0 0 15 15"><path d="M7.5 1l2 4.2 4.5.6-3.3 3.1.8 4.6-4-2.2-4 2.2.8-4.6L1 5.8l4.5-.6z" fill="#ff774c"/></svg>4.2 (30+)</span>
    <span class="meta" style="left:120px;top:204px">
      <svg width="15" height="15" viewBox="0 0 15 15" fill="none" stroke="#ff774c" stroke-width="1.3"><circle cx="7.5" cy="7.5" r="6.3"/><path d="M7.5 4a2.3 2.3 0 0 1 2.3 2.3c0 1.7-2.3 4-2.3 4s-2.3-2.3-2.3-4A2.3 2.3 0 0 1 7.5 4z"/></svg>2.5 Km</span>
    <span class="meta" style="left:210px;top:204px">
      <svg width="15" height="15" viewBox="0 0 15 15" fill="none" stroke="#ff774c" stroke-width="1.3"><circle cx="7.5" cy="7.5" r="6.3"/><path d="M9.3 5.3c-.4-.6-1-.8-1.8-.8-1 0-1.7.5-1.7 1.3 0 1.8 3.6 1 3.6 2.9 0 .8-.8 1.4-1.9 1.4-.9 0-1.6-.4-2-1M7.5 3.5v1M7.5 10.2v1.3"/></svg>25-300</span>
  </article>

  <article class="restaurant-card" style="left:320px">
    <div class="restaurant-photo" role="img" aria-label="Photo of a bright restaurant terrace" style="background:linear-gradient(160deg,#efe6da,#a87a52 55%,#4e3322)"></div>
    <h3 class="restaurant-name">Pizza Restaurant 02</h3>
    <p class="restaurant-address">Address 1234 N St</p>
    <span class="meta" style="left:16px;top:204px">
      <svg width="15" height="15" viewBox="0 0 15 15"><path d="M7.5 1l2 4.2 4.5.6-3.3 3.1.8 4.6-4-2.2-4 2.2.8-4.6L1 5.8l4.5-.6z" fill="#ff774c"/></svg>4.2 (30+)</span>
  </article>

  <nav class="tab-bar" style="top:958px">
    <span class="tab" style="left:62px">
      <svg width="22" height="22" viewBox="0 0 22 22" fill="none" stroke="#9a9da1" stroke-width="1.5"><rect x="2" y="2" width="18" height="18" rx="5"/><path d="M7 9h8M7 13h5" stroke-linecap="round"/></svg>Recipes</span>
    <span class="tab tab--active" style="left:164px">
      <svg width="22" height="22" viewBox="0 0 22 22" fill="none" stroke="#ff774c" stroke-width="1.5"><rect x="3" y="4" width="16" height="16" rx="3"/><path d="M8 2v4M14 2v4M7 15h8M11 8l3 4H8z"/></svg>Restaurant</span>
    <span class="tab" style="left:265px">
      <svg width="24" height="22" viewBox="0 0 24 22" fill="none" stroke="#9a9da1" stroke-width="1.5"><path d="M2 12h20a10 8 0 0 1-20 0zM4 12a8 7 0 0 1 16 0M12 3v2M8 8l2 2M16 8l-2 2"/></svg>Meal</span>
    <span class="tab" style="left:367px">
      <svg width="24" height="22" viewBox="0 0 24 22" fill="none" stroke="#9a9da1" stroke-width="1.5"><circle cx="9" cy="7" r="4"/><path d="M2 20a7 7 0 0 1 14 0zM15 3.5a4 4 0 0 1 0 7M18 14a6 6 0 0 1 4 6h-3"/></svg>Comm</span>
  </nav>
</section>

</body>
</html>
```